Business Card

We need a business card for a fundraising/sales and marketing company called Brightwell Giving services. The logo colours are Red Black and white. The final design should communicate professional, reliable yet fun and charity minded
Updates

Sorry for the delay. A decision will be made in the next 48 hours. we are stuck between two designs. Kind Regards, Laura Dunmore

Industry/Entity Type

Marketing

```html
<!DOCTYPE html>
<html lang="en">
<head>
<meta charset="utf-8">
<title>Brightwell Giving services – Business Card</title>
<link href="https://fonts.googleapis.com/css2?family=Montserrat:wght@500&family=Tinos:wght@400;700&display=swap" rel="stylesheet">
<style>
  :root {
    --backdrop: #e4e4e6;
    --card: #ffffff;
    --brand-red: #d0141c;
    --charcoal: #4a4c4b;
    --ink: #2e2e2e;
    --muted: #555555;
  }
  html, body {
    margin: 0;
    width: 1200px;
    height: 864px;
    overflow: hidden;
    background: var(--backdrop);
  }
  .card {
    position: absolute;
    left: 180px;
    top: 192px;
    width: 840px;
    height: 480px;
    background: var(--card);
    box-shadow: 0 10px 30px rgba(0,0,0,0.18);
    overflow: hidden;
    font-family: "Tinos", "Times New Roman", serif;
  }
  .card-art {
    position: absolute;
    inset: 0;
  }
  .brand {
    position: absolute;
    left: 100px;
    top: 128px;
    display: flex;
    align-items: center;
    gap: 14px;
  }
  .brand-dot {
    width: 22px;
    height: 22px;
    border-radius: 50%;
    background: var(--brand-red);
  }
  .brand-name {
    font-family: "Montserrat", Arial, sans-serif;
    font-weight: 500;
    font-size: 30px;
    letter-spacing: 1px;
    color: var(--charcoal);
  }
  .person {
    position: absolute;
    left: 82px;
    top: 252px;
  }
  .person-name {
    margin: 0;
    font-size: 28px;
    font-weight: 700;
    letter-spacing: 0.5px;
    color: var(--charcoal);
    line-height: 1;
  }
  .person-name .first { color: var(--brand-red); }
  .person-role {
    margin: 4px 0 0;
    font-size: 17px;
    color: var(--muted);
  }
  .contacts {
    position: absolute;
    left: 86px;
    top: 318px;
    margin: 0;
    padding: 0;
    list-style: none;
  }
  .contacts li {
    display: flex;
    align-items: center;
    gap: 14px;
    height: 30px;
    font-size: 21px;
    font-weight: 700;
    color: var(--ink);
    white-space: nowrap;
  }
  .contacts svg { width: 22px; height: 20px; fill: var(--ink); flex: none; }
</style>
</head>
<body>
  <section class="card" aria-label="Brightwell Giving services business card">
    <svg class="card-art" width="840" height="480" viewBox="0 0 840 480" aria-hidden="true">
      <g fill="var(--brand-red)">
        <rect x="0" y="228" width="185" height="6"/>
        <rect x="202" y="228" width="210" height="6"/>
        <rect x="428" y="228" width="185" height="6"/>
        <rect x="630" y="228" width="210" height="6"/>
      </g>
      <polygon fill="var(--charcoal)" points="0,466 460,466 478,418 840,418 840,480 0,480"/>
    </svg>

    <div class="brand">
      <span class="brand-dot"></span>
      <span class="brand-name">Brightwell Giving</span>
    </div>

    <div class="person">
      <h1 class="person-name"><span class="first">DANIEL</span> HARLOW</h1>
      <p class="person-role">Managing Director</p>
    </div>

    <ul class="contacts">
      <li>
        <svg viewBox="0 0 24 22"><path d="M2 7c0-3 5-5 10-5s10 2 10 5v2h-5V7H7v2H2z"/><path d="M5 11h14l2 9H3z"/><circle cx="12" cy="15" r="2.5" fill="#fff"/></svg>
        0044 7821 5036
      </li>
      <li>
        <svg viewBox="0 0 24 22"><rect x="6" y="1" width="12" height="6"/><rect x="1" y="8" width="22" height="9" rx="1"/><rect x="6" y="14" width="12" height="7" fill="#fff" stroke="#2e2e2e" stroke-width="1.5"/></svg>
        0044 7821 5037
      </li>
      <li>
        <svg viewBox="0 0 24 22"><rect x="1" y="3" width="22" height="16"/><path d="M2 4l10 8 10-8M2 18l7-7M22 18l-7-7" stroke="#fff" stroke-width="1.6" fill="none"/></svg>
        hello@brightwellgiving.com
      </li>
      <li>
        <svg viewBox="0 0 24 22"><rect x="1.5" y="2" width="21" height="14" fill="none" stroke="#2e2e2e" stroke-width="2"/><rect x="8" y="18" width="8" height="2.5"/></svg>
        www.brightwellgiving.com
      </li>
    </ul>
  </section>
</body>
</html>
```